Business cards need a revamp and change of address. I have included files of current card which has been used for 5 years. Also a photo of my new store fitout which uses a lot of colour and features inspired by cusco Peru. I would like to see design options with and without the butterfly although I do use the butterfly on my current street signage.
Updates

Reason: would like to see more designers submit

Target Market(s)

women 35 - 65

Industry/Entity Type

Business

Contact Information for Business Card

Larkvale Andean Silver Jewellery & Giftware

Requirements
Must have
• logo frontside
• backside the following text:
• Larkvale Jewellery is hand made using the highest quality 950 Peruvian Silver which is purer than 925 Sterling Silver. Larkvale's range of unique, handcrafted products are directly sourced from fair trade producer co-operatives, individual artisans and artisan groups from Peru, South America.
• Phone 02 43168272
• 7/118 Pelham Road Windsor NSW 2754
• Email : sales@larkvale.com.au
Nice to have
• Like us on face book

```html
<!DOCTYPE html>
<html lang="en">
<head>
<meta charset="utf-8">
<title>Larkvale Business Card</title>
<link href="https://fonts.googleapis.com/css2?family=Didact+Gothic&family=Kaushan+Script&display=swap" rel="stylesheet">
<style>
  :root {
    --backdrop: #d6d6d6;
    --card: #151515;
    --ink: #f2f2f2;
    --ink-soft: #dcdcdc;
    --band-top: #4a4a4a;
    --band-bottom: #2e2e2e;
    --butterfly-a: #3fb1ee;
    --butterfly-b: #1a6fbf;
    --photo-a: #2f8aa0;
    --photo-b: #5a5560;
    --photo-c: #cfd6da;
  }
  * { box-sizing: border-box; margin: 0; padding: 0; }
  html, body { width: 1200px; height: 1000px; overflow: hidden; }
  body {
    background: var(--backdrop);
    font-family: "Didact Gothic", "Century Gothic", sans-serif;
    color: var(--ink);
    position: relative;
  }
  .card {
    position: absolute;
    left: 310px;
    width: 580px;
    height: 323px;
    background: var(--card);
    overflow: hidden;
  }
  .card--front { top: 145px; }
  .card--back { top: 553px; }

  .brand-name {
    position: absolute;
    left: 0; right: 0;
    top: 118px;
    text-align: center;
    font-size: 58px;
    line-height: 1;
    color: var(--ink);
    letter-spacing: 1px;
  }
  .butterfly {
    position: absolute;
    left: 372px;
    top: 173px;
    width: 86px;
    height: 72px;
    border-radius: 40% 40% 45% 45%;
    background: linear-gradient(135deg, var(--butterfly-a), var(--butterfly-b));
  }
  .web-address {
    position: absolute;
    right: 28px;
    bottom: 26px;
    font-size: 14px;
    color: var(--ink);
  }
  .web-address strong { font-weight: 400; font-size: 15px; }

  .heading {
    position: absolute;
    left: 40px;
    top: 38px;
    font-family: "Kaushan Script", cursive;
    font-size: 30px;
    font-weight: 400;
    color: var(--ink);
  }
  .about {
    position: absolute;
    left: 41px;
    top: 102px;
    width: 285px;
    font-size: 13.2px;
    line-height: 16.4px;
    color: var(--ink-soft);
  }
  .store-photo {
    position: absolute;
    left: 377px;
    top: 37px;
    width: 164px;
    height: 185px;
    border: 2px solid #e8e8e8;
    background: linear-gradient(160deg, var(--photo-a) 0%, var(--photo-b) 55%, var(--photo-c) 100%);
  }
  .contact-band {
    position: absolute;
    left: 0; right: 0;
    top: 256px;
    height: 48px;
    background: linear-gradient(to bottom, var(--band-top), var(--band-bottom));
    font-size: 13.5px;
    line-height: 16.5px;
    color: var(--ink);
  }
  .contact-list { position: absolute; left: 43px; top: 8px; }
  .contact-list b { font-weight: 700; }
  .address { position: absolute; left: 377px; top: 8px; font-style: normal; }
</style>
</head>
<body>
  <section class="card card--front" aria-label="Business card front">
    <div class="brand-name">larkvale</div>
    <div class="butterfly" role="img" aria-label="Blue morpho butterfly illustration"></div>
    <div class="web-address">www.<strong>larkvale</strong>.com.au</div>
  </section>

  <section class="card card--back" aria-label="Business card back">
    <h2 class="heading">Peruvian Silver</h2>
    <p class="about">Larkvale Jewellery is hand made using the highest quality 950 Peruvian Silver which is purer than 925 Sterling Silver. Larkvale's range of unique, handcrafted products are directly sourced from fair trade producer co-operatives, individual artisans and artisan groups from Peru, South America.</p>
    <div class="store-photo" role="img" aria-label="Photo of the store interior with pendant lights and glass jewellery cabinets"></div>
    <div class="contact-band">
      <div class="contact-list">
        <div><b>Phone:</b> 02 43168272</div>
        <div><b>Email:</b> sales@larkvale.com.au</div>
      </div>
      <address class="address">7/118 Pelham Road<br>Windsor NSW 2754</address>
    </div>
  </section>
</body>
</html>
```